Poster Required for Cafe to promote coffee/staff discounts

Need an A3 size poster designed for our business to promote that we roast our own coffee, and that we offer discounts for staff.
I have attached a poster which we use to promote catering that our business offers, also have attached logos and our business card..
Also, I have attached our business card I would like the poster to look a little like that.
Eg. Our logo.
Then Specialty Coffee Roasters (under or next to this, in small print: Producing Slow Roasted Coffee)
Location
Download our App
Website
I would like the poster to state:
Tallowmere Health Staff receive $1 off their coffee or hot drink when presenting their staff pass.
Please don't hesitate to ask if you need more info.

```html
<!DOCTYPE html>
<html lang="en">
<head>
<meta charset="utf-8">
<title>Kettle &amp; Crane — Specialty Coffee Roasters</title>
<link rel="stylesheet" href="https://fonts.googleapis.com/css2?family=Josefin+Sans:wght@300;400;600&family=Oswald:wght@300;400;500&family=Arvo:wght@700&display=swap">
<style>
  :root {
    --paper: #fbfb8f;
    --ink: #1d1d1b;
    --ink-soft: #3a3a36;
    --disc: #141516;
    --reverse: #ffffff;
    --bean-dark: #3a1c0e;
    --bean-mid: #6b3518;
    --cup-light: #f1f1ec;
    --coffee: #2a1d14;
  }
  * { margin: 0; padding: 0; box-sizing: border-box; }
  html, body { width: 780px; height: 1200px; overflow: hidden; background: var(--paper); }
  .poster { position: relative; width: 780px; height: 1200px; background: var(--paper); color: var(--ink); }

  .bean-cluster {
    position: absolute;
    border-radius: 50%;
    background: radial-gradient(ellipse at 50% 50%, rgba(107,53,24,0.85) 0%, rgba(58,28,14,0.55) 45%, rgba(58,28,14,0) 72%);
  }
  .bean-cluster--top { left: 108px; top: 78px; width: 130px; height: 130px; }
  .bean-cluster--side { left: 535px; top: 430px; width: 130px; height: 130px; }

  .brand-disc {
    position: absolute; left: 137px; top: 60px; width: 506px; height: 506px;
    border-radius: 50%; background: var(--disc);
  }
  .brand-name {
    position: absolute; left: 137px; width: 506px; top: 262px; text-align: center;
    font-family: "Josefin Sans", sans-serif; font-weight: 300;
    color: var(--reverse); font-size: 58px; line-height: 76px; letter-spacing: 7px;
    text-transform: uppercase;
  }
  .brand-rule {
    position: absolute; left: 366px; top: 518px; width: 48px; height: 3px; background: var(--reverse);
  }

  .headline {
    position: absolute; left: 0; right: 0; top: 620px; text-align: center;
    font-family: "Oswald", sans-serif; font-weight: 500; font-size: 31px; letter-spacing: 2px;
    text-transform: uppercase; line-height: 1;
  }
  .tagline {
    position: absolute; left: 0; right: 0; top: 664px; text-align: center;
    font-family: "Oswald", sans-serif; font-weight: 400; font-size: 12px; letter-spacing: 1.5px;
    text-transform: uppercase;
  }

  .cup {
    position: absolute; left: 295px; top: 698px; width: 190px; height: 190px; border-radius: 50%;
    background: radial-gradient(circle at 50% 50%, var(--coffee) 0%, #8a817a 30%, var(--cup-light) 55%, rgba(241,241,236,0) 100%);
  }

  .staff-offer {
    position: absolute; left: 150px; right: 150px; top: 892px; text-align: center;
    font-family: "Josefin Sans", sans-serif; font-weight: 400; font-size: 16px; line-height: 21px;
  }
  .staff-offer strong { font-weight: 600; }

  .location {
    position: absolute; left: 0; right: 0; top: 940px; text-align: center;
    font-family: "Josefin Sans", sans-serif; font-weight: 300; font-size: 24px; color: var(--ink-soft);
  }
  .region {
    position: absolute; left: 0; right: 0; top: 985px; text-align: center;
    font-family: "Oswald", sans-serif; font-weight: 300; font-size: 15px; letter-spacing: 1px;
    text-transform: uppercase; color: var(--ink-soft);
  }
  .app-button {
    position: absolute; left: 271px; top: 1026px; width: 237px; height: 46px;
    border: 2px solid var(--ink); display: flex; align-items: center; justify-content: center;
    font-family: "Oswald", sans-serif; font-weight: 400; font-size: 20px; letter-spacing: 1px;
    text-transform: uppercase;
  }
  .divider { position: absolute; left: 200px; top: 1097px; }
  .website {
    position: absolute; left: 0; right: 0; top: 1118px; text-align: center;
    font-family: "Arvo", serif; font-weight: 700; font-size: 20px; letter-spacing: 0.5px;
  }
</style>
</head>
<body>
<main class="poster">
  <div class="bean-cluster bean-cluster--top" role="img" aria-label="Scattered roasted coffee beans"></div>
  <div class="bean-cluster bean-cluster--side" role="img" aria-label="Scattered roasted coffee beans"></div>

  <div class="brand-disc"></div>
  <h1 class="brand-name">Kettle &amp;<br>Crane</h1>
  <div class="brand-rule"></div>

  <h2 class="headline">Specialty Coffee Roasters</h2>
  <p class="tagline">Producing slow roasted coffee</p>

  <div class="cup" role="img" aria-label="Photo of a black coffee in a white cup and saucer seen from above"></div>

  <p class="staff-offer"><strong>Tallowmere Health staff receive $1 off</strong> their coffee or hot drink when presenting their staff pass.</p>

  <p class="location">Located at Marlow Hospital</p>
  <p class="region">Queensland, Australia</p>

  <div class="app-button">Download our app</div>

  <svg class="divider" width="380" height="4" viewBox="0 0 380 4" aria-hidden="true">
    <line x1="0" y1="2" x2="380" y2="2" stroke="#1d1d1b" stroke-width="2" stroke-dasharray="7 4"/>
  </svg>

  <p class="website">kettlecrane.com.au</p>
</main>
</body>
</html>
```